website for LanternPeak Advisory - a HR Consultancy Company

Creation of a website template. I would like to make it with with Wix, but am open to other online website programms.

Website is for consulting company in human resources offering the following services:
- Human resources and talent management for small companies
- Human resources consulting for start-ups
- Diversity and Inclusion management/training
- Board of Directors - talent identification and need evalutation
- coaching and counseling

Pages needed:
- Home page
- HR and talent management
- HR consulting for start-ups
- Diversity & Inclusion management/training
- coaching and counseling
- contact

1. My logo below
2. an example website that I like (not in terms of colours): https://www.mapleridgeadvisors.ch/
http://www.veldorquint.ch/

Target Market(s)

small and mid-sized companies, start-ups

Industry/Entity Type

Consulting

Number of Pages Required

5+ page

Font styles to use
Serif
Sans Serif

Colors
3277b5
35a7d7

Requirements
Must have
• - easy on the eye yet professional looking
• - my text is short
• - website should be clear and easy to understand
Nice to have
• - I will include photographs of the coaches
Should not have
• too many colours
• complicated

```html
<!DOCTYPE html>
<html lang="en">
<head>
<meta charset="utf-8">
<title>LanternPeak Advisory – HR Consulting</title>
<link href="https://fonts.googleapis.com/css2?family=Open+Sans:wght@400;600;700&display=swap" rel="stylesheet">
<style>
:root{
  --blue:#1f72b8;
  --blue-dark:#1a5f9c;
  --sky:#35a7d7;
  --ink:#3b3b3b;
  --muted:#777;
  --line:#cfd6dd;
  --paper:#ffffff;
  --mist:#e7e7e7;
  --footer:#666666;
}
*{box-sizing:border-box;margin:0;padding:0}
html,body{width:1200px;height:2875px;overflow:hidden}
body{position:relative;background:var(--paper);font-family:"Open Sans",Arial,sans-serif;color:var(--ink)}
.abs{position:absolute}

/* header */
.site-header{left:0;top:0;width:1200px;height:105px;background:var(--paper)}
.brand{left:155px;top:36px;font-size:22px;font-weight:700;color:var(--blue);letter-spacing:.3px}
.brand-dot{left:130px;top:42px;width:16px;height:16px;border-radius:50%;background:var(--blue)}
.callbar{right:155px;top:20px;display:flex;align-items:center;gap:8px;font-size:14px;color:var(--ink)}
.callbar b{color:var(--blue);font-weight:600}
.social{display:flex;gap:5px}
.social span{width:15px;height:15px;border-radius:50%;background:#555;display:block}
.main-nav{left:380px;top:58px;display:flex;align-items:center;font-size:12.5px;color:var(--ink)}
.main-nav a{color:inherit;text-decoration:none;padding:0 33px;position:relative}
.main-nav a.active{color:var(--blue)}
.main-nav a.active::after{content:"";position:absolute;left:33px;right:33px;bottom:-8px;height:2px;background:var(--blue)}
.main-nav .sep{color:#aaa}
.btn-pill{display:inline-flex;align-items:center;justify-content:center;border-radius:20px;font-weight:600;text-decoration:none}
.btn-consult{left:859px;top:55px;width:186px;height:32px;background:var(--blue);color:#fff;font-size:12.5px}

/* hero */
.hero{left:0;top:105px;width:1200px;height:430px;background:linear-gradient(100deg,#6f7a83 0%,#9aa3aa 40%,#c9cdd0 75%,#e2e2e0 100%)}
.hero-title{left:155px;top:235px;font-size:31px;font-weight:600;color:#fff}
.hero-sub{left:155px;top:282px;font-size:21px;line-height:29px;color:#fff}
.btn-start{left:155px;top:365px;width:128px;height:32px;background:var(--blue);color:#fff;font-size:13px}
.hero-arrow{top:290px;width:24px;height:24px}

/* section headings */
.eyebrow{left:0;width:1200px;text-align:center;font-size:15px;color:var(--muted)}
.heading{left:0;width:1200px;text-align:center;font-size:29px;font-weight:600;color:#444}
.heading em{font-style:normal;color:var(--blue)}
.rule{left:570px;width:60px;height:1px;background:#b8c4cf}

.about-text{left:360px;top:688px;width:480px;text-align:center;font-size:13.5px;line-height:21px;color:var(--muted)}
.link-more{left:0;width:1200px;top:786px;text-align:center;font-size:14px;color:var(--blue)}

.photo-band{left:0;width:1200px;height:400px}
.band-team{top:933px;background:linear-gradient(90deg,#d4d3cf 0%,#8e8a86 35%,#a9a9ad 65%,#dcdcd8 100%)}
.band-meeting{top:1950px;background:linear-gradient(90deg,#c7ccd0 0%,#b8a394 35%,#9fa8c0 60%,#d8dbe0 100%)}

/* services */
.svc-card{top:1494px;width:280px;height:326px;background:var(--blue);color:#fff;overflow:hidden;box-shadow:0 2px 4px rgba(0,0,0,.12)}
.svc-photo{position:absolute;left:0;top:0;width:280px;height:230px}
.svc-cap{position:absolute;left:0;top:230px;width:280px;height:96px;display:flex;align-items:center;justify-content:center;text-align:center;font-size:16px;font-weight:600;line-height:21px;padding:0 20px}
.svc-body{padding:62px 22px 0;text-align:center}
.svc-body h3{font-size:16px;font-weight:600;line-height:22px}
.svc-body p{margin-top:14px;font-size:13px;line-height:21px}
.btn-ghost{margin-top:22px;width:128px;height:32px;border:1.5px solid #fff;color:#fff;font-size:13px}
.svc-arrow{top:1645px;width:26px;height:26px}
.btn-viewall{left:535px;top:1852px;width:130px;height:32px;border:1.5px solid #7fb0d8;color:#555;font-size:13px}

/* contact */
.contact{left:0;top:2350px;width:1200px;height:460px;background:var(--mist)}
.field{background:#fff;border:1px solid var(--line);font-size:10px;color:#666;padding:0 9px;display:flex;align-items:center}
.field-area{align-items:flex-start;padding-top:10px}
.btn-send{left:545px;top:2717px;width:110px;height:32px;background:var(--blue);color:#fff;font-size:13px}

/* footer */
.site-footer{left:0;top:2810px;width:1200px;height:65px;background:var(--footer);color:#eee;font-size:12.5px}
.foot-copy{left:155px;top:24px}
.foot-phone{left:510px;top:24px}
.foot-mail{left:643px;top:24px}
.foot-mail u{color:#fff}
.foot-social{left:957px;top:24px}
.foot-social span{background:#ddd}
</style>
</head>
<body>

<header class="abs site-header">
  <span class="abs brand-dot"></span>
  <div class="abs brand">LanternPeak Advisory</div>
  <div class="abs callbar">
    <b>Call Us:</b>
    <svg width="16" height="16" viewBox="0 0 16 16" aria-hidden="true"><circle cx="8" cy="8" r="7" fill="none" stroke="#1f72b8" stroke-width="1.3"/><path d="M5.3 4.5l1.4 1.6-.8 1.1c.5 1 1.3 1.8 2.3 2.3l1.1-.8 1.6 1.4-.9 1.2C7.7 11 5 8.3 4.7 5.3z" fill="#1f72b8"/></svg>
    <span>123 - 555 - 0142</span>
    <span class="social"><span></span><span></span><span></span><span></span></span>
  </div>
  <nav class="abs main-nav">
    <a class="active">Home</a><span class="sep">|</span>
    <a>About Us</a><span class="sep">|</span>
    <a>Services &nbsp;⌄</a><span class="sep">|</span>
    <a>Contact Us</a>
  </nav>
  <a class="abs btn-pill btn-consult">Ask For Free Consulting</a>
</header>

<section class="abs hero" role="img" aria-label="Photo of a small team gathered around a desk reviewing plans in a bright office"></section>
<h1 class="abs hero-title">LanternPeak Advisory</h1>
<p class="abs hero-sub">Human resources and talent management<br>for small companies</p>
<a class="abs btn-pill btn-start">Get Started</a>
<svg class="abs hero-arrow" style="left:53px" viewBox="0 0 24 24" aria-hidden="true"><circle cx="12" cy="12" r="11" fill="none" stroke="#fff" stroke-width="1.5"/><path d="M14 7l-5 5 5 5" fill="none" stroke="#fff" stroke-width="2"/></svg>
<svg class="abs hero-arrow" style="left:1121px" viewBox="0 0 24 24" aria-hidden="true"><circle cx="12" cy="12" r="11" fill="none" stroke="#fff" stroke-width="1.5"/><path d="M10 7l5 5-5 5" fill="none" stroke="#fff" stroke-width="2"/></svg>

<section class="about">
  <p class="abs eyebrow" style="top:596px">About Us</p>
  <h2 class="abs heading" style="top:615px">Welcome to <em>LanternPeak</em></h2>
  <span class="abs rule" style="top:664px"></span>
  <p class="abs about-text">Contrary to popular belief, Lorem Ipsum is not simply random text. It has roots in a piece of classical Latin literature from 45 BC, making it over 2000 years old. Daniel Marlowe, a Latin professor at Finibus...</p>
  <a class="abs link-more">Discover More →</a>
</section>

<div class="abs photo-band band-team" role="img" aria-label="Photo of colleagues in a casual meeting around a low table with laptops"></div>

<section class="services">
  <p class="abs eyebrow" style="top:1393px">What We Do?</p>
  <h2 class="abs heading" style="top:1412px">Our <em>Services</em></h2>
  <span class="abs rule" style="top:1460px"></span>

  <svg class="abs svc-arrow" style="left:105px" viewBox="0 0 26 26" aria-hidden="true"><circle cx="13" cy="13" r="12" fill="none" stroke="#aaa" stroke-width="1.3"/><path d="M15 8l-5 5 5 5" fill="none" stroke="#aaa" stroke-width="1.8"/></svg>
  <svg class="abs svc-arrow" style="left:1065px" viewBox="0 0 26 26" aria-hidden="true"><circle cx="13" cy="13" r="12" fill="none" stroke="#444" stroke-width="1.3"/><path d="M11 8l5 5-5 5" fill="none" stroke="#444" stroke-width="1.8"/></svg>

  <article class="abs svc-card" style="left:155px">
    <div class="svc-photo" role="img" aria-label="Photo of a smiling business team gathered behind a laptop" style="background:linear-gradient(135deg,#e9e9e9,#8d8a88 60%,#5c5a5a)"></div>
    <h3 class="svc-cap">Human resources &amp; talent management</h3>
  </article>

  <article class="abs svc-card" style="left:460px">
    <div class="svc-body">
      <h3>Human resources consulting<br>for start-ups</h3>
      <p>There are many variations of passages of Lorem Ipsum available, but the majority have...</p>
      <a class="btn-pill btn-ghost">Read More</a>
    </div>
  </article>

  <article class="abs svc-card" style="left:764px">
    <div class="svc-photo" role="img" aria-label="Photo of two businessmen shaking hands in a glass office" style="background:linear-gradient(90deg,#dfe4e8,#9ea7b2 50%,#cfd5da)"></div>
    <h3 class="svc-cap">Diversity &amp; Inclusion management/training</h3>
  </article>

  <a class="abs btn-pill btn-viewall">View All</a>
</section>

<div class="abs photo-band band-meeting" role="img" aria-label="Photo of a team reviewing documents together at a meeting table"></div>

<section class="abs contact"></section>
<p class="abs eyebrow" style="top:2410px">Need Help?</p>
<h2 class="abs heading" style="top:2430px">Contact <em>Us</em></h2>
<span class="abs rule" style="top:2477px"></span>
<form>
  <div class="abs field" style="left:232px;top:2508px;width:360px;height:32px">Name:</div>
  <div class="abs field" style="left:607px;top:2508px;width:360px;height:32px">Phone:</div>
  <div class="abs field" style="left:232px;top:2556px;width:360px;height:32px">Email:</div>
  <div class="abs field" style="left:607px;top:2556px;width:360px;height:32px;justify-content:space-between">Services: <span>⌄</span></div>
  <div class="abs field field-area" style="left:232px;top:2602px;width:735px;height:96px">Massage:</div>
  <a class="abs btn-pill btn-send">Send</a>
</form>

<footer class="abs site-footer">
  <span class="abs foot-copy">©2017 LanternPeak Advisory. All rights reserved</span>
  <span class="abs foot-phone">P.: 123 - 555 - 0142</span>
  <span class="abs foot-mail">E.: <u>info@lanternpeakadvisory.com</u></span>
  <span class="abs social foot-social"><span></span><span></span><span></span><span></span></span>
</footer>

</body>
</html>
```